Business cards for property management company

Need new business cards designed for our property management company and rental community, Amber Knoll Commons. These cards will be primarily picked up by rental applicants.

May be single or double sided design.

I need cards for two different people, listed below. The design can be the same for both, and the only information that will be different is name and email address.

Industry/Entity Type

Property Management

Requirements
Must have
• US standard business card - 2''x3.5'' horizontal design.

1. Logo (attached). The text does not have to stay below the logo, but the card does need to say "Amber Knoll Commons" somewhere on it (does not have to be same font as logo, but those fonts are Americana Extra Bold and BlackJack if needed).
2. Name: one with "Lena Halvorsen" and one with "Dorian Halvorsen"
3. Email address: one with "lena@amberknollhub.com" and one with "dorian@amberknollhub.com"
4. Web address: amberknollhub.com
5. Phone: 503.555.0182
6. Address: 7390 Whitlock Avenue, Brenton, Oregon 97512 (zip code may me omitted, at your discretion)
Should not have
• No rounded corners or special cuts.

No bevel, emboss or shadow effects.

As a note, please do not use our website as a basis for color or design schemes. We are working on a redesign, based around the new logo (attached to brief).

```html
<!DOCTYPE html>
<html lang="en">
<head>
<meta charset="utf-8">
<title>Amber Knoll Commons — Business Card</title>
<link rel="stylesheet" href="https://fonts.googleapis.com/css2?family=Montserrat:wght@400;500;600;700&display=swap">
<style>
  :root {
    --backdrop: #e9ece6;
    --card-white: #ffffff;
    --brand-green: #4a9a2c;
    --brand-blue: #1593c4;
    --text-light: #ffffff;
  }
  * { margin: 0; padding: 0; box-sizing: border-box; }
  html, body {
    width: 1200px;
    height: 798px;
    overflow: hidden;
    background: var(--backdrop);
    font-family: "Montserrat", Arial, sans-serif;
  }
  .canvas {
    position: relative;
    width: 1200px;
    height: 798px;
  }
  .business-card {
    position: absolute;
    left: 100px;
    top: 113px;
    width: 1000px;
    height: 572px;
    background: var(--card-white);
    overflow: hidden;
  }
  .card-bands {
    position: absolute;
    inset: 0;
    width: 1000px;
    height: 572px;
  }
  .band-green { fill: var(--brand-green); }
  .band-blue { fill: var(--brand-blue); }

  .brand-lockup {
    position: absolute;
    left: 60px;
    top: 250px;
    width: 340px;
    display: flex;
    align-items: center;
    gap: 16px;
  }
  .brand-dot {
    flex: none;
    width: 34px;
    height: 34px;
    border-radius: 50%;
    background: var(--brand-blue);
  }
  .brand-name {
    font-weight: 700;
    font-size: 34px;
    line-height: 1.1;
    color: var(--brand-green);
  }

  .contact-block {
    position: absolute;
    right: 56px;
    top: 0;
    height: 572px;
    color: var(--text-light);
    text-align: right;
  }
  .person {
    position: absolute;
    right: 0;
    top: 78px;
    white-space: nowrap;
  }
  .person-name {
    font-weight: 600;
    font-size: 34px;
    letter-spacing: 0.5px;
  }
  .person-email {
    font-weight: 400;
    font-size: 22px;
    margin-top: 4px;
  }
  .details {
    position: absolute;
    right: 0;
    bottom: 64px;
    white-space: nowrap;
    font-size: 22px;
    line-height: 1.45;
  }
  .phone { margin-bottom: 18px; font-weight: 500; }
  .website { margin-top: 18px; font-weight: 700; font-size: 24px; }
</style>
</head>
<body>
<main class="canvas">
  <article class="business-card">
    <svg class="card-bands" viewBox="0 0 1000 572" aria-hidden="true">
      <path class="band-green" d="M 640 0 Q 470 260 420 572 L 450 572 Q 500 266 670 0 Z"/>
      <path class="band-blue" d="M 682 0 Q 512 270 462 572 L 1000 572 L 1000 0 Z"/>
    </svg>

    <div class="brand-lockup">
      <span class="brand-dot"></span>
      <span class="brand-name">Amber Knoll Commons</span>
    </div>

    <div class="contact-block">
      <div class="person">
        <p class="person-name">Lena Halvorsen</p>
        <p class="person-email">lena@amberknollhub.com</p>
      </div>
      <div class="details">
        <p class="phone">503.555.0182</p>
        <p class="address">7390 Whitlock Avenue,</p>
        <p class="address">Brenton, Oregon 97512</p>
        <p class="website">www.amberknollhub.com</p>
      </div>
    </div>
  </article>
</main>
</body>
</html>
```